Horizontal scrolling homepage | ||
Consulting company needing a unique layout | ||
Consulting | ||
Qorvinex does consulting and implementation projects within CRM which are the processes around sales, marketing, service, call centers, web shops and more. Even though such engagements of course need the technical involvement from IT, it for sure also needs the business and in this segment the business consists of extrovert colorful people. |
The homepage must be different than the competitors and one way of doing that is by having horizontal scrolling with a menu bar on the left (if the design would be better, you can place it on the top). If it can be done in a cool way, then the left menu bar could be a bit to the right of the left border so that the scrolling background is visible. The scrolling should accelerate and de-accelerate when moving to the part of the homepage that should be displayed. There should not be a scrollbar. Menu: Start (or logo) Packages Services Next Step Career About On the start page there should be a combined sign up for newsletter and contact form (like here: brimtala[dot]dk[slash]om-brimtala). (Title, first name, last name, e-mail, mobile phone number, checkbox for Newsletter sign up and a free text field). The homepage must be easy to extend with additional texts. There should be teasers on the start page that will navigate the user to a place on one of the subpages with more information. It could be interesting to have flipping boxes like in Window Mobile, where one side of the box has a teaser one-liner and when the mouse hovers over it flips and the solution is on the back and when clicked, the page scrolls to the place with more information. But I do not know how easy that will be to implement with HTML5. Inspire me. In addition add the content that normally is part of a start page. You will find logo and teasers as attachments. For additional text use dummy latin. |
Cutting-Edge Unique/Creative Flashy Professional Corporate Modern Elegant Service Oriented |
See logo | ||
Arial Verdana Trebuchet MS |
left side | ||
http://www.morvenquaily.co.uk/ | ||
http://www.pravessa.com/ | ||
http://tunbelfield.com/ | ||
The homepage should be compatible with Internet Explorer and Crome, it should be accessible from Android pads and phones and Apple Iphones and Ipads, but I assume that will all automatically be possible when HTML5 is used for the development. The homepage must be easy to extend with additional menu items / texts. |

```html
<!DOCTYPE html>
<html lang="en">
<head>
<meta charset="utf-8">
<title>Qorvinex – Start</title>
<link rel="stylesheet" href="https://fonts.googleapis.com/css2?family=Arimo:wght@400;700&display=swap">
<style>
:root{
  --blue:#1f6fae;
  --blue-dark:#17507f;
  --blue-text:#2a7cc0;
  --green:#4aa82c;
  --grey-bg:#d9dcdf;
  --grey-panel:#eceeef;
  --grey-text:#8a8f94;
  --num:#5a7fa6;
  --ink:#4d5560;
  --white:#ffffff;
}
*{margin:0;padding:0;box-sizing:border-box}
html,body{width:1200px;height:490px;overflow:hidden;background:var(--white);font-family:"Arimo",Arial,sans-serif}
.page{position:relative;width:1200px;height:490px}

/* header */
.brand{position:absolute;left:26px;top:18px;display:flex;align-items:center;gap:8px}
.brand-dot{width:28px;height:28px;border-radius:50%;background:var(--blue)}
.brand-name{font-size:30px;font-weight:700;color:var(--blue)}

.main-nav{position:absolute;left:330px;top:44px;display:flex;gap:30px}
.nav-item{display:flex;gap:6px;align-items:flex-start}
.nav-icon{width:18px;height:18px;border-radius:50%;background:linear-gradient(#8fb8d8,var(--blue));margin-top:1px}
.nav-label{font-size:13px;font-weight:700;color:var(--ink);text-transform:uppercase;line-height:1.1}
.nav-sub{display:block;font-size:9px;font-weight:400;color:var(--grey-text);text-transform:none}

.sales{position:absolute;left:620px;top:4px;display:flex;gap:8px;align-items:center}
.sales-text{font-size:12px;color:var(--green);line-height:1.15}
.sales-phone{font-size:18px;color:var(--ink);display:block}

/* stage */
.stage{position:absolute;left:0;top:80px;width:1200px;height:376px;background:linear-gradient(#e9ebed,var(--grey-bg))}
.tab{position:absolute;top:0;height:376px;display:flex;flex-direction:column;justify-content:space-between;align-items:center;padding:14px 0 10px}
.tab-text{writing-mode:vertical-rl;transform:rotate(180deg);font-size:17px;line-height:1.15;color:var(--blue-text)}
.tab-num{font-size:24px;font-weight:700;color:var(--num)}
.tab-intro{left:0;width:100px;background:var(--grey-panel)}
.tab-intro .accent{color:var(--green)}
.tab-active{left:100px;width:112px;background:linear-gradient(var(--blue),var(--blue-dark))}
.tab-active .tab-text{color:var(--white)}
.tab-active .tab-num{background:var(--white);color:var(--blue);padding:2px 8px;margin-left:-40px}

.feature{position:absolute;left:212px;top:0;width:578px;height:376px}
.feature-photo{position:absolute;inset:0;background:linear-gradient(90deg,#c9d2da,#e4dcd6 55%,#cfd6dd)}
.feature-card{position:absolute;left:62px;top:42px;width:266px;height:278px;background:rgba(255,255,255,.82);padding:16px}
.feature-title{font-size:17px;line-height:1.3;color:var(--blue-text);font-weight:400;margin-bottom:10px}
.feature-card p{font-size:13px;line-height:1.38;color:#3e4750;margin-bottom:10px}

.tab-small{width:54px;background:rgba(255,255,255,.78)}
.tab-small .tab-text{font-size:16px}
.tab-small .tab-num{font-size:22px}

.next-arrow{position:absolute;left:1050px;top:160px}
.contact-tab{position:absolute;right:0;top:178px;width:32px;height:120px;background:var(--green);display:flex;align-items:center;justify-content:center}
.contact-tab span{writing-mode:vertical-rl;transform:rotate(180deg);color:var(--white);font-weight:700;font-size:12px;letter-spacing:.5px}

.copyright{position:absolute;right:160px;top:468px;font-size:9px;color:#555}
</style>
</head>
<body>
<div class="page">
  <header>
    <div class="brand"><span class="brand-dot"></span><span class="brand-name">Qorvinex</span></div>
    <div class="sales">
      <svg width="22" height="22" viewBox="0 0 24 24"><path fill="#d84a3a" d="M6.6 10.8a15 15 0 0 0 6.6 6.6l2.2-2.2c.3-.3.7-.4 1-.2 1.1.4 2.3.6 3.6.6.6 0 1 .4 1 1V20c0 .6-.4 1-1 1A17 17 0 0 1 3 4c0-.6.4-1 1-1h3.5c.6 0 1 .4 1 1 0 1.3.2 2.5.6 3.6.1.3 0 .7-.2 1z"/></svg>
      <div class="sales-text">For sales enquiry<span class="sales-phone">+45 3217 4480</span></div>
    </div>
    <nav class="main-nav">
      <div class="nav-item"><span class="nav-icon"></span><span class="nav-label">Packages<span class="nav-sub">what we offer</span></span></div>
      <div class="nav-item"><span class="nav-icon"></span><span class="nav-label">Services<span class="nav-sub">what we provide</span></span></div>
      <div class="nav-item"><span class="nav-icon"></span><span class="nav-label">Next Step<span class="nav-sub">what we have now</span></span></div>
      <div class="nav-item"><span class="nav-icon"></span><span class="nav-label">Careers<span class="nav-sub">future with us</span></span></div>
      <div class="nav-item"><span class="nav-icon"></span><span class="nav-label">About Us<span class="nav-sub">who we are</span></span></div>
    </nav>
  </header>

  <main class="stage">
    <section class="tab tab-intro">
      <span class="tab-text">Talvero projects are big and costly, <span class="accent">right?</span><br>Well, they don't have to be.</span>
      <span class="tab-num">01</span>
    </section>
    <section class="tab tab-active">
      <span class="tab-text">Looking for a system to control your<br>marketing, sale or service processes?</span>
      <span class="tab-num">02</span>
    </section>
    <section class="feature">
      <div class="feature-photo" role="img" aria-label="Photo of a smiling businesswoman"></div>
      <div class="feature-card">
        <h2 class="feature-title">Looking for a system to control your marketing, sale or service processes?</h2>
        <p>Then Talvero's combined setup of software to a reduced price, and delivery, called Swift Rollout Services, is your solution.</p>
        <p>Qorvinex has already delivered this concept in the Nordic; contact us for a discussion of how you can gain and grow from this.</p>
      </div>
    </section>
    <section class="tab tab-small" style="left:796px"><span class="tab-text">Need something special for your<br>Talvero implementation?</span><span class="tab-num">03</span></section>
    <section class="tab tab-small" style="left:856px"><span class="tab-text">Realise your most important asset,<br>your employees and customers!</span><span class="tab-num">04</span></section>
    <section class="tab tab-small" style="left:916px"><span class="tab-text">How can we help you realise?<br>Planning on a new sales drive...</span><span class="tab-num">05</span></section>
    <section class="tab tab-small" style="left:976px"><span class="tab-text">Collaborate!<br>Optimize your sales projects...</span><span class="tab-num">06</span></section>
    <svg class="next-arrow" width="40" height="60" viewBox="0 0 40 60"><path d="M8 6 32 30 8 54" fill="none" stroke="#ffffff" stroke-width="7"/></svg>
  </main>

  <a class="contact-tab"><span>CONTACT US</span></a>
  <footer class="copyright">copyright Qorvinex 2012. all right reserved.</footer>
</div>
</body>
</html>
```